Bluewater Products Flyer

Bluewater Lending Group, Inc.
Licensed Mortgage Company
Serving the DMV since 1997
"You choose Bluewater, we'll carry it home"
We specialize in...
FHA Loans
* Credit Scores as low as 500
* 203K Renovation Loans
Conventional Loans
* As little as 1% Down
* Bank Statement for Self-Employed
Investor Loans
* DSCR, & Fix & Flip
* Commercial & New Construction
Other Programs
* HELOCS & Reverse Mortgages
Call today for a free consultation
(800) 641-2957
www.bluewaterlendhub.com
NMLS #731846

```html
<!DOCTYPE html>
<html lang="en">
<head>
<meta charset="utf-8">
<title>Bluewater Lending Group – Products Flyer</title>
<link href="https://fonts.googleapis.com/css2?family=Cinzel:wght@500;600&family=Playfair+Display:ital,wght@1,700&family=Lora:wght@400&family=Outfit:wght@400;600;700&display=swap" rel="stylesheet">
<style>
:root{
  --artboard:#999999;
  --navy:#0c1a22;
  --ocean:#0f5a8c;
  --ocean-deep:#0a3f66;
  --lime:#a6cf3a;
  --gold:#c2a93f;
  --orange:#d3922b;
  --ink:#1b1d22;
  --charcoal:#333230;
  --sand:#e2dbaa;
  --paper:#f8f8f8;
  --white:#ffffff;
}
*{margin:0;padding:0;box-sizing:border-box}
html,body{width:1058px;height:1200px;overflow:hidden;background:var(--artboard)}
.flyer{position:absolute;left:134px;top:95px;width:780px;height:1009px;background:var(--paper);overflow:hidden;font-family:"Outfit",sans-serif;color:var(--ink)}
.hero{position:absolute;left:0;top:0;width:780px;height:444px;background:linear-gradient(120deg,var(--ocean-deep) 0%,var(--ocean) 55%,#1a6a9a 100%)}
.hero-photo{position:absolute;inset:0}
.brand-banner{position:absolute;left:39px;top:0;width:233px;height:198px;background:var(--navy);clip-path:polygon(0 0,100% 0,100% 88%,50% 100%,0 88%);display:flex;flex-direction:column;align-items:center;justify-content:center;gap:10px;padding-bottom:20px}
.brand-name{display:flex;align-items:center;gap:8px;font-family:"Cinzel",serif;font-weight:600;font-size:25px;color:var(--gold);letter-spacing:1px}
.brand-dot{width:14px;height:14px;border-radius:50%;background:var(--gold)}
.brand-est{font-family:"Outfit",sans-serif;font-size:8px;letter-spacing:2px;color:var(--white)}
.headline{position:absolute;left:0;top:335px;width:780px;text-align:center;font-family:"Cinzel",serif;font-weight:500;font-size:46px;color:var(--white);letter-spacing:1px}
.subline{position:absolute;left:0;top:385px;width:780px;display:flex;align-items:center;justify-content:center;gap:14px;font-family:"Playfair Display",serif;font-style:italic;font-weight:700;font-size:29px;color:var(--white)}
.subline .rule{width:87px;height:1px;background:var(--white)}
.stripe{position:absolute;left:0;top:446px;width:780px;height:5px;display:flex}
.stripe .blue{width:392px;background:var(--ocean)}
.stripe .gold{flex:1;background:var(--gold)}
.specialize{position:absolute;left:0;top:484px;width:780px;display:flex;align-items:center;justify-content:center;gap:10px;font-family:"Lora",serif;font-size:37px;color:var(--ink)}
.specialize .rule{width:61px;height:2px;background:var(--orange)}
.card{position:absolute;top:583px;width:223px;height:215px;border:1.5px solid;border-radius:9px;padding:56px 0 0 29px}
.card--fha{left:50px;border-color:var(--ocean)}
.card--conv{left:287px;border-color:var(--lime)}
.card--inv{left:524px;border-color:var(--gold)}
.card-badge{position:absolute;left:25px;top:-44px;width:85px;height:85px;border-radius:50%;display:flex;align-items:center;justify-content:center}
.card--fha .card-badge{background:var(--ocean)}
.card--conv .card-badge{background:var(--lime)}
.card--inv .card-badge{background:var(--gold)}
.card-title{font-weight:600;font-size:24px;line-height:30px;margin-bottom:10px}
.card-list{list-style:none}
.card-list li{position:relative;padding-left:23px;font-size:17px;line-height:21px;margin-bottom:6px}
.card-list li svg{position:absolute;left:0;top:3px}
.other{position:absolute;left:0;top:810px;width:780px;display:flex;align-items:center;justify-content:center;gap:12px;font-size:19px}
.other strong{font-weight:600}
.other .bar{width:1px;height:23px;background:var(--orange)}
.call-band{position:absolute;left:0;top:885px;width:780px;height:58px;background:var(--charcoal);display:flex;align-items:center;justify-content:center;gap:16px;color:var(--white);font-weight:700;font-size:26px}
.call-phone{display:flex;align-items:center;gap:8px;color:var(--lime)}
.footer{position:absolute;left:0;top:943px;width:780px;height:66px;background:var(--sand);display:flex;align-items:center;justify-content:center;gap:14px;font-size:23px;font-weight:500;color:var(--charcoal)}
.footer .bar{width:1px;height:24px;background:var(--gold)}
</style>
</head>
<body>
<main class="flyer">
  <section class="hero">
    <div class="hero-photo" role="img" aria-label="Photograph of a smiling family of four, toned in blue"></div>
    <div class="brand-banner">
      <div class="brand-name"><span class="brand-dot"></span>Bluewater</div>
      <div class="brand-est">EST. 1997</div>
    </div>
    <h1 class="headline">You choose Bluewater</h1>
    <p class="subline"><span class="rule"></span>We'll carry it home<span class="rule"></span></p>
  </section>
  <div class="stripe"><span class="blue"></span><span class="gold"></span></div>

  <h2 class="specialize"><span class="rule"></span>We specialize in<span class="rule"></span></h2>

  <article class="card card--fha">
    <div class="card-badge">
      <svg width="40" height="46" viewBox="0 0 40 46" fill="none" stroke="#fff" stroke-width="2"><rect x="6" y="3" width="28" height="38" rx="2"/><path d="M11 12h18M11 18h18M11 24h18M11 30h12"/><circle cx="8" cy="38" r="6" fill="#0f5a8c"/><path d="M5 38l2 2 4-4"/></svg>
    </div>
    <h3 class="card-title">FHA Loans</h3>
    <ul class="card-list">
      <li><svg width="14" height="14" viewBox="0 0 14 14"><circle cx="7" cy="7" r="7" fill="#0f5a8c"/><path d="M4 7l2 2 4-4" stroke="#fff" stroke-width="1.6" fill="none"/></svg>Credit Scores as low as 500</li>
      <li><svg width="14" height="14" viewBox="0 0 14 14"><circle cx="7" cy="7" r="7" fill="#0f5a8c"/><path d="M4 7l2 2 4-4" stroke="#fff" stroke-width="1.6" fill="none"/></svg>203K Renovation Loans</li>
    </ul>
  </article>

  <article class="card card--conv">
    <div class="card-badge">
      <svg width="48" height="48" viewBox="0 0 48 48" fill="none" stroke="#fff" stroke-width="2"><path d="M12 20L24 9l12 11"/><rect x="15" y="19" width="18" height="14" rx="2"/><path d="M24 22v8M21 24h5M21 28h5"/><path d="M4 40h10l10 3 16-7"/></svg>
    </div>
    <h3 class="card-title">Conventional Loans</h3>
    <ul class="card-list">
      <li><svg width="14" height="14" viewBox="0 0 14 14"><circle cx="7" cy="7" r="7" fill="#0f5a8c"/><path d="M4 7l2 2 4-4" stroke="#fff" stroke-width="1.6" fill="none"/></svg>As little as 1% Down</li>
      <li><svg width="14" height="14" viewBox="0 0 14 14"><circle cx="7" cy="7" r="7" fill="#0f5a8c"/><path d="M4 7l2 2 4-4" stroke="#fff" stroke-width="1.6" fill="none"/></svg>Bank Statement for Self-Employed</li>
    </ul>
  </article>

  <article class="card card--inv">
    <div class="card-badge">
      <svg width="50" height="46" viewBox="0 0 50 46" fill="none" stroke="#fff" stroke-width="2"><circle cx="30" cy="16" r="10"/><path d="M30 10v12M27 13h5M27 19h5"/><path d="M4 30h10l12 6 18-8"/></svg>
    </div>
    <h3 class="card-title">Investor Loans</h3>
    <ul class="card-list">
      <li><svg width="14" height="14" viewBox="0 0 14 14"><circle cx="7" cy="7" r="7" fill="#0f5a8c"/><path d="M4 7l2 2 4-4" stroke="#fff" stroke-width="1.6" fill="none"/></svg>DSCR, &amp; Fix &amp; Flip</li>
      <li><svg width="14" height="14" viewBox="0 0 14 14"><circle cx="7" cy="7" r="7" fill="#0f5a8c"/><path d="M4 7l2 2 4-4" stroke="#fff" stroke-width="1.6" fill="none"/></svg>Commercial &amp; New Construction</li>
    </ul>
  </article>

  <p class="other"><strong>Other Programs</strong><span class="bar"></span>HELOCS &amp; Reverse Mortgages</p>

  <section class="call-band">
    <span>Call today for a free consultation</span>
    <span class="call-phone">
      <svg width="26" height="26" viewBox="0 0 26 26" fill="none" stroke="#a6cf3a" stroke-width="2"><circle cx="13" cy="13" r="12"/><path d="M9 7l2 3-1.5 1.5c1 2 2.5 3.5 4.5 4.5L15.5 14l3 2-1 2.5c-5 0-10-5-10-10z"/></svg>
      (800) 641-2957
    </span>
  </section>

  <footer class="footer">
    <span>www.bluewaterlendhub.com</span><span class="bar"></span><span>NMLS #731846</span>
  </footer>
</main>
</body>
</html>
```